I would like to start a new webpage for a dating site in switzerland.
The dating site is not a escort service at all and should not transmit any type of sexual connotation.
The is more a compagnionship dating : male pay to meet ladies for some time in which they invite them for dinner, coktail, museum visit or walking or even skying. the meeting will take place in big cities in switzerland: geneva, zurich, bern, lausannes.

Industry/Entity Type

Dating

```html
<!DOCTYPE html>
<html lang="en">
<head>
<meta charset="utf-8">
<title>Swiss Companion — Companionship Dating</title>
<link rel="stylesheet" href="https://fonts.googleapis.com/css2?family=Roboto:wght@300;400;500;700&display=swap">
<style>
:root{
  --pink:#e9496c;
  --pink-dark:#d63a5d;
  --pink-form:#f36d8c;
  --pink-field:#f891aa;
  --page:#f3f1f2;
  --ink:#333;
  --muted:#555;
  --white:#fff;
  --orange:#f7931e;
  --line:#ddd;
}
*{box-sizing:border-box;margin:0;padding:0}
html,body{width:753px;height:1200px;overflow:hidden;background:var(--page)}
body{font-family:"Roboto",Arial,sans-serif;color:var(--ink)}
.page{position:relative;width:753px;height:1200px;overflow:hidden}

/* header */
.site-header{position:absolute;left:0;top:0;width:753px;height:53px;background:var(--pink);border-top:3px solid #f2708d}
.brand{position:absolute;left:120px;top:14px;display:flex;align-items:center;gap:6px;color:var(--white);font-weight:700;font-size:15px}
.brand-dot{width:28px;height:28px;border-radius:50%;background:var(--white)}
.call{position:absolute;right:115px;top:10px;color:var(--white);font-size:13px}
.call b{font-size:14px}
.main-nav{position:absolute;right:116px;top:33px;display:flex;gap:24px}
.main-nav a{color:var(--white);font-size:8px;text-decoration:none;font-weight:500}

/* hero */
.hero-photo{position:absolute;left:0;top:53px;width:753px;height:323px;background:linear-gradient(100deg,#c9b9b0 0%,#e7ddd6 35%,#bfb6ae 60%,#d9d6d2 100%)}
.slide-arrow{position:absolute;top:229px;width:32px;height:32px;border-radius:50%;background:rgba(255,255,255,.45)}
.slide-arrow svg{position:absolute;left:10px;top:9px}
.features{position:absolute;left:124px;top:261px;width:274px;height:115px;background:rgba(255,255,255,.82);padding:12px 15px}
.features h2{font-size:14px;font-weight:700;color:#333}
.feature-list{display:grid;grid-template-columns:86px 106px 60px;row-gap:6px;margin-top:9px;list-style:none}
.feature-list li{font-size:8px;font-weight:700;display:flex;align-items:center;gap:5px}
.btn-info{position:absolute;left:17px;top:70px;width:148px;height:20px;background:var(--orange);border-radius:2px;color:#222;font-size:10px;font-weight:500;text-align:center;line-height:20px}

.signup{position:absolute;left:449px;top:82px;width:189px;height:294px;background:var(--white)}
.signup-panel{position:absolute;left:0;top:0;width:189px;height:224px;background:var(--pink-form);border:5px solid #f79ab0;padding:12px 0 0 17px;color:var(--white)}
.signup-panel h3{font-size:11.5px;font-weight:700;line-height:15px;white-space:nowrap;letter-spacing:-0.2px}
.signup-panel h3 .light{font-weight:400}
.signup-panel h3 .line2{font-size:12px}
.field-label{position:absolute;font-size:7px}
.field{position:absolute;height:15px;background:var(--pink-field);border:1px solid #fbb6c6;font-size:7px;color:var(--white);padding:3px 4px}
.field.select::after{content:"";position:absolute;right:4px;top:5px;border:3px solid transparent;border-top-color:var(--white)}
.btn-send{position:absolute;left:111px;top:181px;width:54px;height:24px;background:var(--white);color:var(--pink);font-size:12px;text-align:center;line-height:24px}
.heart-mark{position:absolute;left:12px;top:210px}
.callback{position:absolute;left:17px;top:229px;font-size:10.5px;color:#555;line-height:13px;width:170px}
.callback em{font-style:normal;color:var(--pink)}
.callback-phone{position:absolute;left:82px;top:259px;font-size:13px;font-weight:500;color:var(--pink)}
.callback-arrow{position:absolute;left:42px;top:256px}
.hero-band{position:absolute;left:0;top:376px;width:753px;height:6px;background:var(--pink-dark)}

/* section titles */
.section-title{position:absolute;left:0;width:753px;text-align:center;font-size:16px;font-weight:400;color:#333}
.title-rule{position:absolute;top:418px;height:1px;background:#ccc}
.carousel-btn{position:absolute;top:412px;width:12px;height:12px;background:var(--pink-form)}
.carousel-btn svg{position:absolute;left:3px;top:3px}

/* profiles */
.profile{position:absolute;top:445px;text-align:center}
.profile-photo{height:123px;border:1px solid #ddd}
.profile-name{font-size:8px;color:#333;margin-top:4px}
.profile-meta{font-size:6px;font-weight:700;color:var(--pink);margin-top:2px}
.profile-rule{height:2px;background:var(--pink-form);margin-top:4px}
.divider{position:absolute;left:0;width:753px;height:1px;background:#e2dfe0}

/* advantages */
.advantage{position:absolute;top:687px;width:118px}
.advantage-photo{height:70px}
.advantage h4{font-size:12.5px;font-weight:400;margin-top:14px;color:#222}
.advantage p{font-size:7.3px;line-height:10.5px;color:#333;margin-top:2px}
.read-more{display:flex;align-items:center;gap:4px;font-size:7px;font-weight:500;margin-top:7px}

/* info row */
.info-col{position:absolute;top:936px}
.info-col h5{font-size:12px;font-weight:400;color:#222}
.info-col p{font-size:7.3px;line-height:10.5px;color:#333;margin-top:3px;text-align:justify}
.accordion{list-style:none;margin-top:6px;width:133px}
.accordion li{font-size:7px;font-weight:500;height:22.5px;line-height:22px;border-bottom:1px solid #ddd;display:flex;justify-content:space-between}
.member-grid{display:grid;grid-template-columns:repeat(3,44px);gap:6px 6px;margin-top:6px}
.member-thumb{height:35px}
.btn-view{width:44px;height:14px;background:#999;color:var(--white);font-size:6px;text-align:center;line-height:14px;margin-top:6px}
.input{border:1px solid #e0e0e0;background:var(--white);font-size:6.5px;color:#999;padding:3px}
.btn-small-send{position:absolute;left:85px;top:142px;width:59px;height:14px;background:var(--pink);color:var(--white);font-size:6px;text-align:center;line-height:14px}

/* footer */
.site-footer{position:absolute;left:0;top:1108px;width:753px;height:92px;background:var(--pink);border-top:3px solid #f2708d}
.social{position:absolute;top:14px;width:19px;height:19px;border-radius:50%;background:var(--white)}
.footer-nav{position:absolute;top:47px;left:0;width:753px;display:flex;justify-content:center;gap:28px}
.footer-nav a{color:var(--white);font-size:7.5px;text-decoration:none}
.footer-rule{position:absolute;top:65px;left:0;width:753px;height:1px;background:#f07a95}
.copyright{position:absolute;top:74px;width:753px;text-align:center;color:var(--white);font-size:5.5px}
</style>
</head>
<body>
<div class="page">

  <header class="site-header">
    <div class="brand"><span class="brand-dot"></span>SWISS COMPANION</div>
    <div class="call">CALL US: <b>022 555 0142</b></div>
    <nav class="main-nav">
      <a href="#">ABOUT US</a><a href="#">DATING</a><a href="#">ADD PROFILE</a><a href="#">COMMUNITY</a><a href="#">CONTACT US</a>
    </nav>
  </header>

  <div class="hero-photo" role="img" aria-label="Photo of a couple embracing, the woman holding a red rose"></div>
  <div class="slide-arrow" style="left:71px"><svg width="12" height="14"><path d="M8 2 L3 7 L8 12" stroke="#fff" stroke-width="2" fill="none"/></svg></div>
  <div class="slide-arrow" style="left:651px"><svg width="12" height="14"><path d="M4 2 L9 7 L4 12" stroke="#fff" stroke-width="2" fill="none"/></svg></div>

  <section class="features">
    <h2>ENJOY WITH YOUR DATING ON:</h2>
    <ul class="feature-list">
      <li><svg width="9" height="8"><path d="M1 4 L3.5 7 L8 1" stroke="#e9496c" stroke-width="2" fill="none"/></svg>DINNER</li>
      <li><svg width="9" height="8"><path d="M1 4 L3.5 7 L8 1" stroke="#e9496c" stroke-width="2" fill="none"/></svg>MUSEUM VISIT</li>
      <li><svg width="9" height="8"><path d="M1 4 L3.5 7 L8 1" stroke="#e9496c" stroke-width="2" fill="none"/></svg>COCKTAIL</li>
      <li><svg width="9" height="8"><path d="M1 4 L3.5 7 L8 1" stroke="#e9496c" stroke-width="2" fill="none"/></svg>SKYING</li>
      <li><svg width="9" height="8"><path d="M1 4 L3.5 7 L8 1" stroke="#e9496c" stroke-width="2" fill="none"/></svg>WALKING</li>
    </ul>
    <div class="btn-info">GET MORE INFORMATION</div>
  </section>

  <aside class="signup">
    <div class="signup-panel">
      <h3>JOIN ITS FREE.<br><span class="line2"><span class="light">AND </span>START DATING <span class="light">TODAY</span></span></h3>
      <span class="field-label" style="left:19px;top:46px">I am</span>
      <span class="field-label" style="left:93px;top:46px">Seeking</span>
      <div class="field select" style="left:19px;top:59px;width:67px">Woman</div>
      <div class="field select" style="left:93px;top:59px;width:72px">Man</div>
      <span class="field-label" style="left:19px;top:84px">Country:</span>
      <div class="field select" style="left:19px;top:96px;width:146px">Switzerland</div>
      <div class="field" style="left:19px;top:123px;width:146px">Zip Code:</div>
      <div class="field" style="left:19px;top:153px;width:146px">E-mail:</div>
      <div class="btn-send">SEND</div>
    </div>
    <svg class="heart-mark" width="24" height="20"><path d="M12 19 C2 12 0 8 2 4 C4 0 10 1 12 5 C14 1 20 0 22 4 C24 8 22 12 12 19Z" fill="#fff"/></svg>
    <p class="callback"><em>or</em> you may call us to schedule a DATING</p>
    <svg class="callback-arrow" width="36" height="14"><path d="M2 2 C6 12 20 12 32 9" stroke="#999" fill="none"/><path d="M29 6 L33 9 L29 12" stroke="#999" fill="none"/></svg>
    <div class="callback-phone">022 555 0142</div>
  </aside>
  <div class="hero-band"></div>

  <div class="carousel-btn" style="left:119px"><svg width="6" height="6"><path d="M4 0 L1 3 L4 6" stroke="#fff" fill="none"/></svg></div>
  <div class="title-rule" style="left:136px;width:144px"></div>
  <h2 class="section-title" style="top:408px">LAST ADDED PROFILE</h2>
  <div class="title-rule" style="left:462px;width:160px"></div>
  <div class="carousel-btn" style="left:626px"><svg width="6" height="6"><path d="M2 0 L5 3 L2 6" stroke="#fff" fill="none"/></svg></div>

  <article class="profile" style="left:118px;width:123px">
    <div class="profile-photo" role="img" aria-label="Profile photo of Christina with a coffee cup" style="background:linear-gradient(135deg,#d9d2cc,#8a7a70)"></div>
    <div class="profile-name">Christina</div><div class="profile-meta">Age: 22, Switzerland</div><div class="profile-rule"></div>
  </article>
  <article class="profile" style="left:255px;width:120px">
    <div class="profile-photo" role="img" aria-label="Profile photo of Allisa by a pool" style="background:linear-gradient(135deg,#6fc9dc,#8a5a3e)"></div>
    <div class="profile-name">Allisa</div><div class="profile-meta">Age: 26, Switzerland</div><div class="profile-rule"></div>
  </article>
  <article class="profile" style="left:389px;width:119px">
    <div class="profile-photo" role="img" aria-label="Profile photo of Samantha in sunglasses by a pool" style="background:linear-gradient(135deg,#2b8fb0,#c9a77a)"></div>
    <div class="profile-name">Samantha</div><div class="profile-meta">Age: 36, Switzerland</div><div class="profile-rule"></div>
  </article>
  <article class="profile" style="left:519px;width:119px">
    <div class="profile-photo" role="img" aria-label="Profile photo of Brittany" style="background:linear-gradient(135deg,#e3dcc9,#8b6a52)"></div>
    <div class="profile-name">Brittany</div><div class="profile-meta">Age: 21, Switzerland</div><div class="profile-rule"></div>
  </article>

  <div class="divider" style="top:630px"></div>

  <h2 class="section-title" style="top:656px">OUR AGENCY ADVANTAGES</h2>

  <article class="advantage" style="left:119px">
    <div class="advantage-photo" role="img" aria-label="Photo of a woman in a warm coat" style="background:linear-gradient(135deg,#e9e4df,#8c6a52)"></div>
    <h4>DON'T STAY ALONE</h4>
    <p>Lorem ipsum dolor sit amasdfaet, consec tetur adipiscing elit, sead do eiusmod tempor incididunt ut labore et dolore magna aliqua. Ut enim ad minsasids fim veniam, quis nostrud exsiercitati on ullamco laboris nisi ut aliquip fiex ea commodo consequat.</p>
    <div class="read-more"><svg width="10" height="9"><path d="M5 9 C1 6 0 4 1 2 C2 0 4 0 5 2 C6 0 8 0 9 2 C10 4 9 6 5 9Z" fill="#e02a2a"/></svg>READ MORE</div>
  </article>
  <article class="advantage" style="left:252px">
    <div class="advantage-photo" role="img" aria-label="Photo of a couple close together at sunset" style="background:linear-gradient(135deg,#f0c9a0,#7a5040)"></div>
    <h4>SUCCESS STORIES</h4>
    <p>Lorem ipsum dolor sit amsdfgset, consec tetur adipiscing elit, sead do eiusmod tempor incididunt ut labore et dolore magna aliqua. Ut enim ad minsasids fim veniam, quis nostrud exsiercitati on ullamco laboris nisi ut aliquip fiex ea commodo consequat.</p>
    <div class="read-more"><svg width="10" height="9"><path d="M5 9 C1 6 0 4 1 2 C2 0 4 0 5 2 C6 0 8 0 9 2 C10 4 9 6 5 9Z" fill="#e02a2a"/></svg>READ MORE</div>
  </article>
  <article class="advantage" style="left:385px">
    <div class="advantage-photo" role="img" aria-label="Photo of a smiling couple outdoors" style="background:linear-gradient(135deg,#e8e2dc,#a88a70)"></div>
    <h4>DATING GUIDE</h4>
    <p>Lorem ipsum dolor sit amsdfget, consec tetur adipiscing elit, sed do eiusmod tempor incididunt ut labore et dolore magna aliqua. Ut enim ad minsasids fim veniam, quis nostrud exsiercitati on ullamco laboris nisi ut aliquip fiex ea commodo consequat.</p>
    <div class="read-more"><svg width="10" height="9"><path d="M5 9 C1 6 0 4 1 2 C2 0 4 0 5 2 C6 0 8 0 9 2 C10 4 9 6 5 9Z" fill="#e02a2a"/></svg>READ MORE</div>
  </article>
  <article class="advantage" style="left:521px">
    <div class="advantage-photo" role="img" aria-label="Photo of a couple at a cafe table" style="background:linear-gradient(135deg,#d8d0c8,#7a4a3a)"></div>
    <h4>INTERNATIONAL</h4>
    <p>Lorem ipsum dolor sit amsdfghet, consec tetur adipiscing elit, sed do eiusmod tempor incididunt ut labore et dolore magna aliqua. Ut enim ad minsasids fim veniam, quis nostrud exsiercitati on ullamco laboris nisi ut aliquip fiex ea commodo consequat.</p>
    <div class="read-more"><svg width="10" height="9"><path d="M5 9 C1 6 0 4 1 2 C2 0 4 0 5 2 C6 0 8 0 9 2 C10 4 9 6 5 9Z" fill="#e02a2a"/></svg>READ MORE</div>
  </article>

  <div class="divider" style="top:910px"></div>

  <section class="info-col" style="left:119px;width:136px">
    <h5>POPULAR INFO</h5>
    <p>Lorem ipsum dolor sit amasdfaet, consec tetur adipiscing elit, sead do eiusmod tempor incididunt ut labore et dolore magna aliqua. Ut enim ad minsasids.</p>
    <ul class="accordion">
      <li>FRESH VIDEO<span>+</span></li>
      <li>NEWS &amp; EVENTS<span>+</span></li>
      <li>OUR RULES<span>+</span></li>
      <li>LINKS<span>+</span></li>
    </ul>
  </section>

  <section class="info-col" style="left:296px;width:150px">
    <h5>MEMBERS ONLINE NOW</h5>
    <div class="member-grid">
      <div class="member-thumb" role="img" aria-label="Member photo" style="background:#c9a48c"></div>
      <div class="member-thumb" role="img" aria-label="Member photo" style="background:#6e5548"></div>
      <div class="member-thumb" role="img" aria-label="Member photo" style="background:#7bb5c9"></div>
      <div class="member-thumb" role="img" aria-label="Member photo" style="background:#b0604e"></div>
      <div class="member-thumb" role="img" aria-label="Member photo" style="background:#8d7468"></div>
      <div class="member-thumb" role="img" aria-label="Member photo" style="background:#c89c7c"></div>
      <div class="member-thumb" role="img" aria-label="Member photo" style="background:#b98c70"></div>
      <div class="member-thumb" role="img" aria-label="Member photo" style="background:#5e4a44"></div>
      <div class="member-thumb" role="img" aria-label="Member photo" style="background:#d2ad94"></div>
    </div>
    <div class="btn-view">VIEW ALL</div>
  </section>

  <section class="info-col" style="left:479px;width:145px">
    <h5>QUICK MESSAGE</h5>
    <p>Lorem ipsum dolor sit amasdfaet, cosec tetur adipiscing elit, sead.</p>
    <div class="input" style="width:144px;height:14px;margin-top:6px">Your name</div>
    <div class="input" style="width:144px;height:69px;margin-top:5px">Message</div>
    <div class="btn-small-send">SEND</div>
  </section>

  <footer class="site-footer">
    <span class="social" style="left:324px"></span>
    <span class="social" style="left:353px"></span>
    <span class="social" style="left:381px"></span>
    <span class="social" style="left:409px"></span>
    <nav class="footer-nav">
      <a href="#">About Us</a><a href="#">Dating</a><a href="#">Add Profile</a><a href="#">Community</a><a href="#">Contact Us</a>
    </nav>
    <div class="footer-rule"></div>
    <p class="copyright">Copyright 2014. <b>SWISSCOMPANION</b>. All Right Reserved.</p>
  </footer>

</div>
</body>
</html>
```